Brightwater Communications

I need a very clean, uncomplicated design for an LA-based, very senior level strategic communications firm with about four associates. Landing page should stress LA, maybe a slider with downtown skyline, Corvana pier, and Tamsen Drive. In addition to landing page with firm's description, all else we'd need is services offered page and another for bios of associates.

Industry/Entity Type

Communications

Font styles to use
Sans Serif

```html
<!DOCTYPE html>
<html lang="en">
<head>
<meta charset="utf-8">
<title>Brightwater Communications</title>
<link href="https://fonts.googleapis.com/css2?family=Open+Sans:wght@400;600;700&family=Roboto:wght@400;500;700;900&display=swap" rel="stylesheet">
<style>
:root{
  --blue:#1b74e4;
  --blue-band:#4b9ee0;
  --dark:#333333;
  --darker:#2b2b2b;
  --mid:#5e5e5e;
  --text:#3a3a3a;
  --muted:#8a8a8a;
  --line:#cfcfcf;
  --field:#f4f4f4;
  --panel:#dcdcdc;
  --white:#ffffff;
}
*{box-sizing:border-box;margin:0;padding:0}
html,body{width:1088px;height:1200px;overflow:hidden;background:var(--white)}
body{position:relative;font-family:"Open Sans",Arial,sans-serif;color:var(--text)}
.abs{position:absolute}
svg{display:block}

/* top bar */
.topbar{left:0;top:0;width:1088px;height:24px;background:var(--dark);color:#e6e6e6;font-size:11.5px}
.topbar .item{position:absolute;top:5px;display:flex;align-items:center;gap:6px}
.topbar .account{right:156px;top:5px;position:absolute}

/* header */
.brand{left:156px;top:36px;display:flex;align-items:center;gap:12px}
.brand-mark{width:62px;height:62px;border-radius:50%;background:var(--blue)}
.brand-name{font-family:"Roboto",Arial,sans-serif;font-weight:500;font-size:26px;line-height:27px;color:var(--blue)}
.search{left:655px;top:50px;width:279px;height:30px;border:1px solid var(--line);background:#fafafa;font-size:12px;color:#aaa;padding:7px 10px}
.search svg{position:absolute;right:10px;top:6px}

/* hero */
.band{left:0;top:110px;width:1088px;height:285px;background:var(--blue-band)}
.hero{left:156px;top:110px;width:778px;height:352px;background:linear-gradient(180deg,#7fb0dc 0%,#b8cfe0 30%,#8f9aa2 55%,#6e6660 75%,#9b8a7c 100%);box-shadow:0 4px 8px rgba(0,0,0,.35)}
.headline{font-family:"Roboto",Arial,sans-serif;font-weight:700;color:var(--white);background:var(--blue);text-transform:uppercase;white-space:nowrap}
.headline.one{left:175px;top:184px;height:44px;padding:0 7px;font-size:38px;line-height:44px}
.headline.two{left:175px;top:230px;height:40px;padding:0 7px;font-size:27px;line-height:40px}
.cta{left:178px;top:280px;width:288px;height:35px;background:linear-gradient(#3a3a3a,#0d0d0d);border:1px solid #666;border-radius:3px;color:#fff;font-family:"Roboto",Arial,sans-serif;font-weight:500;font-size:18px;line-height:33px;text-align:center}
.quote-panel{left:700px;top:172px;width:234px;height:280px;background:rgba(170,205,240,.72)}
.quote-title{left:682px;top:139px;width:233px;height:35px;background:var(--darker);color:#fff;font-weight:700;font-size:14.5px;line-height:35px;padding-left:52px;clip-path:polygon(0 0,100% 0,100% 100%,0 100%,18px 50%)}
.field{background:#fff;border:1px solid #d8d8d8;border-radius:3px;font-size:11.5px;color:#9a9a9a;padding:7px 10px}
.field svg{position:absolute;right:10px;top:9px}
.btn-outline{border:1px solid var(--blue);border-radius:4px;color:var(--blue);font-family:"Roboto",Arial,sans-serif;font-weight:700;font-size:12px;display:flex;align-items:center;justify-content:center;gap:5px;background:#fff}
.btn-submit-hero{left:837px;top:386px;width:69px;height:26px;background:transparent;color:#fff;border-color:#fff}

/* welcome */
.welcome-title{left:156px;top:488px;font-family:"Roboto",Arial,sans-serif;font-weight:700;font-size:21px;color:#222;white-space:nowrap}
.welcome-title span{color:var(--blue)}
.welcome-copy{left:160px;top:519px;width:384px;font-size:11px;line-height:15.3px;letter-spacing:-0.2px;color:var(--text)}
.welcome-copy p+p{margin-top:15px}
.btn-view{width:83px;height:27px;margin-top:14px;margin-left:-1px;letter-spacing:0}

.card{top:491px;width:184px;height:199px;color:#eee;overflow:hidden}
.card.webinar{left:566px;background:var(--mid)}
.card.testimonial{left:750px;background:var(--dark)}
.card h3{position:absolute;top:16px;font-family:"Roboto",Arial,sans-serif;font-weight:700;font-size:16px;color:#fff;white-space:nowrap}
.card .copy{position:absolute;font-size:10.8px;line-height:15px;z-index:1}
.card .more{position:absolute;font-size:11px;color:#fff}

/* partners */
.partners-tab{left:156px;top:726px;width:149px;height:20px;background:var(--panel)}
.partners{left:156px;top:742px;width:778px;height:135px;background:var(--panel)}
.partners-title{left:160px;top:730px;font-family:"Roboto",Arial,sans-serif;font-weight:700;font-size:19px;color:#222}
.partners-title span{color:var(--blue)}
.slide-arrow{top:796px;width:27px;height:27px;background:var(--blue);display:flex;align-items:center;justify-content:center}
.partner{top:773px;width:118px;height:74px;background:#ececec;border:1px solid #b9b9b9;display:flex;align-items:center;justify-content:center}
.partner-badge{width:54px;height:32px;border-radius:4px;background:#9a9a9a}

/* lower columns */
.col-title{font-family:"Roboto",Arial,sans-serif;font-weight:500;font-size:14px;color:#222;display:flex;align-items:center;gap:8px;white-space:nowrap}
.col-title span{color:var(--blue)}
.footer-field{background:var(--field);border:1px solid #dadada;font-size:11px;color:#a3a3a3;padding:7px 9px}
.footer-field svg{position:absolute;right:9px;top:8px}
.news-item{left:409px;width:256px}
.news-item h4{font-family:"Roboto",Arial,sans-serif;font-weight:700;font-size:11px;color:#222;white-space:nowrap}
.news-item p{font-size:10.8px;line-height:15px;letter-spacing:-0.15px;color:#666;margin-top:3px}
.news-item .more{display:block;text-align:right;font-size:11px;color:var(--blue);margin-top:2px}
.contact-row{left:705px;display:flex;gap:12px;font-size:10.5px;line-height:13px;color:#333}
.social{top:1043px;width:22px;height:22px;border-radius:50%;background:#e3e3e3}

/* footer */
.footer-line{left:0;top:1123px;width:1088px;height:4px;background:var(--blue)}
.footer{left:0;top:1130px;width:1088px;height:70px;background:var(--dark);color:#eee;font-size:11px;text-align:center;line-height:68px}
</style>
</head>
<body>

<div class="abs topbar">
  <div class="item" style="left:158px">
    <svg width="11" height="11" viewBox="0 0 24 24"><path fill="#ddd" d="M6.6 10.8a15 15 0 0 0 6.6 6.6l2.2-2.2c.3-.3.7-.4 1-.2 1.1.4 2.3.6 3.6.6.6 0 1 .4 1 1V20c0 .6-.4 1-1 1A17 17 0 0 1 3 4c0-.6.4-1 1-1h3.5c.6 0 1 .4 1 1 0 1.3.2 2.5.6 3.6.1.3 0 .7-.2 1z"/></svg>
    +0800 555 0142
  </div>
  <div class="item" style="left:276px">
    <svg width="12" height="10" viewBox="0 0 24 18"><rect x="1" y="1" width="22" height="16" rx="2" fill="none" stroke="#ddd" stroke-width="2"/><path d="M1 2l11 8 11-8" fill="none" stroke="#ddd" stroke-width="2"/></svg>
    info@brightwatercomms.com
  </div>
  <div class="account">Login &nbsp;|&nbsp; Register</div>
</div>

<div class="abs brand">
  <div class="brand-mark"></div>
  <div class="brand-name">brightwater<br>communications</div>
</div>

<div class="abs search">Search
  <svg width="17" height="17" viewBox="0 0 24 24"><circle cx="10" cy="10" r="7" fill="none" stroke="#1b74e4" stroke-width="3"/><path d="M15 15l6 6" stroke="#1b74e4" stroke-width="3" stroke-linecap="round"/></svg>
</div>

<div class="abs band"></div>
<div class="abs hero" role="img" aria-label="Photo of the downtown Los Angeles skyline under a blue sky with mountains behind"></div>

<div class="abs headline one">The Guide in a Labyrinth</div>
<div class="abs headline two">of Communication Solutions!</div>
<div class="abs cta">CLICK HERE FOR MORE DETAIL</div>

<div class="abs quote-panel"></div>
<div class="abs quote-title">Get Started Today</div>

<div class="abs field" style="left:710px;top:194px;width:195px;height:30px">Name*
  <svg width="10" height="11" viewBox="0 0 20 22"><circle cx="10" cy="6" r="5" fill="#9a9a9a"/><path d="M0 22c0-6 4-9 10-9s10 3 10 9z" fill="#9a9a9a"/></svg></div>
<div class="abs field" style="left:710px;top:226px;width:195px;height:30px">Email
  <svg width="12" height="10" viewBox="0 0 24 18"><rect width="24" height="18" rx="2" fill="#9a9a9a"/><path d="M1 2l11 8 11-8" fill="none" stroke="#fff" stroke-width="2"/></svg></div>
<div class="abs field" style="left:710px;top:258px;width:195px;height:30px">Phone number
  <svg width="10" height="10" viewBox="0 0 24 24"><path fill="#9a9a9a" d="M6.6 10.8a15 15 0 0 0 6.6 6.6l2.2-2.2c.3-.3.7-.4 1-.2 1.1.4 2.3.6 3.6.6.6 0 1 .4 1 1V20c0 .6-.4 1-1 1A17 17 0 0 1 3 4c0-.6.4-1 1-1h3.5c.6 0 1 .4 1 1 0 1.3.2 2.5.6 3.6.1.3 0 .7-.2 1z"/></svg></div>
<div class="abs field" style="left:710px;top:290px;width:195px;height:87px">Message
  <svg width="12" height="10" viewBox="0 0 24 20"><path d="M2 2h14v9H7l-4 3v-3H2z" fill="#9a9a9a"/><path d="M18 6h4v9h-1v3l-4-3h-7v-2h8z" fill="#9a9a9a"/></svg></div>
<div class="abs btn-outline btn-submit-hero">Submit
  <svg width="11" height="11" viewBox="0 0 24 24"><circle cx="12" cy="12" r="11" fill="#fff"/><path d="M8 12h8M13 8l4 4-4 4" fill="none" stroke="#7aaee0" stroke-width="2.5"/></svg></div>

<h1 class="abs welcome-title">Welcome to <span>Brightwater Communication</span></h1>
<div class="abs welcome-copy">
  <p>Nunc malesuada mauris quis neque egestas ullamcorper at quis magna. Sed eget turpis ipsum. Etiam eget augue ut turpis semper volutpat ut non dolor. Maecenas a nibh ac elit faucibus vestibulum ut quis sem. Duis dictum justo non eleifend consequat. Curabitur a malesuada turpis. Nam vitae convallis dolor, ut malesuada neque. Curabitur blandit posuere aliquam. Sed porttitor ultricies iaculis. Ut dapibus rutrum lectus.</p>
  <p>Ut mattis a est eget luctus. Nulla interdum metus vitae turpis rhoncus, id porta nibh bibendum. Maecenas consequat malesuada arcu sed consectetur.</p>
  <div class="btn-outline btn-view">View more
    <svg width="11" height="11" viewBox="0 0 24 24"><circle cx="12" cy="12" r="11" fill="#1b74e4"/><path d="M8 12h8M13 8l4 4-4 4" fill="none" stroke="#fff" stroke-width="2.5"/></svg></div>
</div>

<section class="abs card webinar">
  <svg class="abs" style="left:5px;top:6px" width="33" height="33" viewBox="0 0 34 34"><circle cx="17" cy="17" r="16" fill="#3d8fe0"/><circle cx="17" cy="17" r="16" fill="none" stroke="#9cc8f2" stroke-width="2"/></svg>
  <h3 style="left:47px">Free Webinar</h3>
  <div class="abs" style="left:7px;top:49px;width:169px;height:63px;background:linear-gradient(135deg,#e8f2fb,#7fb6e6 60%,#3f7fc0)" role="img" aria-label="Illustration of laptops connected to a central globe network"></div>
  <p class="copy" style="left:8px;top:120px;width:170px">Etiam ex mi, ultrices eget nisl vitae, iaculis consectetur diam. Donec condimentum ex vel</p>
  <span class="more" style="left:9px;top:165px">Read more »</span>
</section>

<section class="abs card testimonial">
  <div class="abs" style="left:100px;top:120px;width:84px;height:79px;background:linear-gradient(180deg,#5a5a5a,#b9c4cf)" role="img" aria-label="Portrait photo of the client giving the testimonial"></div>
  <svg class="abs" style="left:8px;top:10px" width="28" height="24" viewBox="0 0 28 24"><path d="M14 1C6.8 1 1 5.4 1 10.5c0 3 1.9 5.6 4.9 7.3L4 23l6.3-3.5c1.2.2 2.4.4 3.7.4 7.2 0 13-4.3 13-9.4S21.2 1 14 1z" fill="#8fd0f5"/></svg>
  <h3 style="left:42px">Client Testimonial</h3>
  <p class="copy" style="left:16px;top:49px;width:164px">Proin ut aliquet diam. Etiam ex mi, ultrices eget nisl vitae, iaculis consectetur diam. Donec condimentum ex vel neque vehicula hendrerit.</p>
  <p class="copy" style="left:18px;top:132px;color:#fff">Proin Interdum<br>CEO, Sed eget</p>
</section>

<div class="abs partners-tab"></div>
<div class="abs partners" role="img" aria-label="Light grey panel with a faint communication-device pattern"></div>
<h2 class="abs partners-title">OUR <span>PARTNERS</span></h2>
<div class="abs slide-arrow" style="left:156px"><svg width="10" height="14" viewBox="0 0 10 14"><path d="M8 1L2 7l6 6" fill="none" stroke="#fff" stroke-width="2"/></svg></div>
<div class="abs slide-arrow" style="left:908px"><svg width="10" height="14" viewBox="0 0 10 14"><path d="M2 1l6 6-6 6" fill="none" stroke="#fff" stroke-width="2"/></svg></div>
<div class="abs partner" style="left:205px"><div class="partner-badge"></div></div>
<div class="abs partner" style="left:345px"><div class="partner-badge"></div></div>
<div class="abs partner" style="left:485px"><div class="partner-badge"></div></div>
<div class="abs partner" style="left:626px"><div class="partner-badge"></div></div>
<div class="abs partner" style="left:765px"><div class="partner-badge"></div></div>

<!-- newsletter -->
<div class="abs col-title" style="left:156px;top:905px">
  <svg width="22" height="28" viewBox="0 0 22 28"><path d="M5 12V8a6 6 0 0 1 12 0v4" fill="none" stroke="#999" stroke-width="2.5"/><rect x="1" y="12" width="20" height="15" rx="2" fill="#d7d7d7" stroke="#aaa"/></svg>
  <span style="color:#222">Newsletter</span><span style="margin-left:-4px">Signup</span>
</div>
<div class="abs footer-field" style="left:156px;top:953px;width:207px;height:28px">Name
  <svg width="9" height="10" viewBox="0 0 20 22"><circle cx="10" cy="6" r="5" fill="#bbb"/><path d="M0 22c0-6 4-9 10-9s10 3 10 9z" fill="#bbb"/></svg></div>
<div class="abs footer-field" style="left:156px;top:1000px;width:207px;height:28px">Email
  <svg width="11" height="9" viewBox="0 0 24 18"><rect width="24" height="18" rx="2" fill="#bbb"/><path d="M1 2l11 8 11-8" fill="none" stroke="#fff" stroke-width="2"/></svg></div>
<div class="abs" style="left:158px;top:1036px;width:88px;height:62px;background:linear-gradient(160deg,#f2f2f2,#c9c9c9)" role="img" aria-label="Photo of a folded stack of newspapers"></div>
<div class="abs btn-outline" style="left:295px;top:1044px;width:68px;height:27px">Submit
  <svg width="11" height="11" viewBox="0 0 24 24"><circle cx="12" cy="12" r="11" fill="#1b74e4"/><path d="M8 12h8M13 8l4 4-4 4" fill="none" stroke="#fff" stroke-width="2.5"/></svg></div>

<!-- news -->
<div class="abs col-title" style="left:408px;top:904px">
  <svg width="24" height="26" viewBox="0 0 24 26"><rect x="1" y="1" width="20" height="24" fill="#eee" stroke="#999"/><path d="M5 7h12M5 11h12M5 15h12M5 19h8" stroke="#aaa" stroke-width="1.5"/></svg>
  <span style="color:#222">News &amp;</span><span style="margin-left:-4px">Updates</span>
</div>
<article class="abs news-item" style="top:946px">
  <h4>Proin ut aliquet diam. Etiam ex mi, ultrices eget nisl</h4>
  <p>Donec condimentum ex vel neque vehicula hendrerit. Proin interdum vehicula eleifend.</p>
  <span class="more">Read more »</span>
</article>
<div class="abs" style="left:409px;top:1011px;width:256px;border-top:1px dashed #bbb"></div>
<article class="abs news-item" style="top:1020px">
  <h4>Proin ut aliquet diam. Etiam ex mi, ultrices eget nisl</h4>
  <p>Donec condimentum ex vel neque vehicula hendrerit. Proin interdum vehicula eleifend.</p>
  <span class="more">Read more »</span>
</article>

<!-- contact -->
<div class="abs col-title" style="left:704px;top:905px">
  <svg width="26" height="24" viewBox="0 0 26 24"><path d="M1 9L13 1l12 8v14H1z" fill="#eee" stroke="#999"/><path d="M1 9l12 8 12-8" fill="none" stroke="#999"/></svg>
  <span style="color:#222">Contact</span><span style="margin-left:-4px">Us</span>
</div>
<div class="abs contact-row" style="top:948px">
  <svg width="13" height="12" viewBox="0 0 24 22"><path d="M12 1L1 11h3v10h6v-6h4v6h6V11h3z" fill="#1b74e4"/></svg>
  <span>52, Etiam sit amet magna nec quam venen<br>atis vehicula ut sed nisl.</span>
</div>
<div class="abs contact-row" style="top:983px">
  <svg width="12" height="12" viewBox="0 0 24 24"><path fill="#1b74e4" d="M6.6 10.8a15 15 0 0 0 6.6 6.6l2.2-2.2c.3-.3.7-.4 1-.2 1.1.4 2.3.6 3.6.6.6 0 1 .4 1 1V20c0 .6-.4 1-1 1A17 17 0 0 1 3 4c0-.6.4-1 1-1h3.5c.6 0 1 .4 1 1 0 1.3.2 2.5.6 3.6.1.3 0 .7-.2 1z"/></svg>
  <span>+0800 555 0142</span>
</div>
<div class="abs contact-row" style="top:1009px">
  <svg width="12" height="10" viewBox="0 0 24 18" style="margin-top:2px"><rect width="24" height="18" rx="2" fill="#1b74e4"/><path d="M1 2l11 8 11-8" fill="none" stroke="#fff" stroke-width="2"/></svg>
  <span>hello@brightwatercomms.com</span>
</div>
<div class="abs social" style="left:705px"></div>
<div class="abs social" style="left:736px"></div>
<div class="abs social" style="left:767px"></div>
<div class="abs social" style="left:798px"></div>

<div class="abs footer-line"></div>
<footer class="abs footer">Copyright © 2014, all rights reserved.</footer>

</body>
</html>
```